Saltmarsh Courier Ad

I would Like to design a newspaper ad for a local paper I have attached a copy of what Ive used in the past as a jumping off point. Please be creative this is a high end location so please keep it elegant as well. the size needs to be 10" x 15.875"

I would like it to list services but not like it is right now, I don't need to have every specific thing that I do per service just an overview of what I actually do

Target Market(s)

Client clientele on Block island

Requirements
Must have
• I would like to see pictures as well as the list of services and any other suggestions you feel maybe important to have. Please utilize my website for ideas on what you can add to the ad. www.tidewellnb.com

```html
<!DOCTYPE html>
<html lang="en">
<head>
<meta charset="utf-8">
<title>Tidewell Pool Service – Saltmarsh Courier Ad</title>
<link href="https://fonts.googleapis.com/css2?family=Roboto+Condensed:wght@400;500;700&family=Lato:wght@400;700&display=swap" rel="stylesheet">
<style>
  :root{
    --navy:#0d2d6c;
    --navy-deep:#0a2558;
    --orange:#f26b21;
    --orange-light:#f7931e;
    --orange-deep:#e2502a;
    --paper:#f4f4f5;
    --rim:#b9bbbf;
    --stage:#c9cacd;
    --ink:#2b2b2b;
    --white:#ffffff;
  }
  *{box-sizing:border-box;margin:0;padding:0}
  html,body{width:1200px;height:1200px;overflow:hidden;background:var(--stage)}
  .ad{
    position:absolute;left:222px;top:0;width:858px;height:1362px;
    transform:scale(0.881);transform-origin:0 0;
    background:linear-gradient(180deg,#fbfbfb 0%,var(--paper) 40%,#e9eaeb 70%,#f4f4f4 100%);
    overflow:hidden;font-family:'Roboto Condensed',sans-serif;
  }
  .ad-art{position:absolute;left:0;top:0;width:858px;height:1362px}
  .brand{position:absolute;left:38px;top:62px;display:flex;align-items:center;gap:12px}
  .brand-dot{width:26px;height:26px;border-radius:50%;background:var(--orange)}
  .brand-name{font-family:'Roboto Condensed',sans-serif;font-weight:700;color:var(--navy);font-size:30px;line-height:1.05;letter-spacing:.5px}
  .headline{position:absolute;left:302px;top:40px;text-transform:uppercase;line-height:1}
  .headline-top{display:block;color:var(--navy);font-weight:400;font-size:49px;letter-spacing:-.3px}
  .headline-main{display:block;color:var(--orange);font-weight:700;font-size:52px;margin-top:6px;letter-spacing:-.2px}
  .benefits{position:absolute;left:37px;top:830px;width:385px}
  .benefits h2{color:var(--navy);font-weight:500;font-size:21px;line-height:26px;text-transform:uppercase}
  .benefits ul{list-style:none;margin-top:18px}
  .benefits li{position:relative;padding-left:18px;font-family:'Lato',sans-serif;font-size:14.5px;line-height:19px;color:var(--ink);margin-bottom:19px;text-align:justify}
  .benefits li::before{content:"";position:absolute;left:0;top:4px;width:9px;height:9px;border:1.5px solid var(--navy);border-radius:50%}
  .services{position:absolute;left:476px;top:818px;width:307px;height:313px;background:var(--navy);border-radius:30px;padding:38px 16px 0 16px}
  .services h3{color:var(--orange);font-weight:500;font-size:21px;text-transform:uppercase}
  .services ul{list-style:none;margin-top:15px}
  .services li{display:flex;align-items:center;gap:10px;color:var(--white);font-size:16px;font-weight:500;text-transform:uppercase;height:20px;margin-bottom:21px}
  .services li svg{flex:none}
  .contact{position:absolute;left:267px;top:1249px;color:var(--white);font-size:16px;font-weight:500;line-height:20px;text-transform:uppercase}
  .contact .web{text-transform:none}
  .offer{position:absolute;right:51px;top:1242px;text-align:right;color:var(--navy);font-size:22px;font-weight:500;line-height:27px;text-transform:uppercase}
  .social{position:absolute;left:752px;top:1304px;display:flex;gap:10px}
  .social span{width:20px;height:20px;background:var(--navy);border-radius:2px}
  .social span+span{background:#c8202a}
</style>
</head>
<body>
<div class="ad">
  <svg class="ad-art" viewBox="0 0 858 1362" xmlns="http://www.w3.org/2000/svg">
    <defs>
      <linearGradient id="orangeFill" x1="0" y1="0" x2="1" y2="1">
        <stop offset="0" stop-color="var(--orange-light)"/>
        <stop offset="1" stop-color="var(--orange-deep)"/>
      </linearGradient>
      <linearGradient id="poolPhoto" x1="0" y1="0" x2="0" y2="1">
        <stop offset="0" stop-color="#3f6b34"/>
        <stop offset="0.27" stop-color="#5f8f45"/>
        <stop offset="0.33" stop-color="#d9cfb4"/>
        <stop offset="0.4" stop-color="#5cc9d3"/>
        <stop offset="1" stop-color="#2fb3c3"/>
      </linearGradient>
      <linearGradient id="spaPhoto" x1="0" y1="0" x2="1" y2="1">
        <stop offset="0" stop-color="#b7b4ad"/>
        <stop offset="0.4" stop-color="#5b6a45"/>
        <stop offset="0.7" stop-color="#8a7a5e"/>
        <stop offset="1" stop-color="#d8e4e6"/>
      </linearGradient>
      <linearGradient id="portraitPhoto" x1="0" y1="0" x2="1" y2="1">
        <stop offset="0" stop-color="#7a6a58"/>
        <stop offset="0.5" stop-color="#c99a7e"/>
        <stop offset="1" stop-color="#3f8fa6"/>
      </linearGradient>
      <clipPath id="clipLower"><rect x="0" y="490" width="400" height="400"/></clipPath>
      <clipPath id="clipUpper"><rect x="700" y="120" width="158" height="250"/></clipPath>
    </defs>

    <!-- corner swooshes -->
    <g clip-path="url(#clipUpper)">
      <circle cx="597" cy="484" r="368" fill="var(--rim)"/>
      <circle cx="597" cy="484" r="360" fill="url(#orangeFill)"/>
    </g>
    <g clip-path="url(#clipLower)">
      <circle cx="235" cy="400" r="380" fill="var(--rim)"/>
      <circle cx="235" cy="400" r="372" fill="url(#orangeFill)"/>
    </g>

    <!-- photo rings -->
    <circle cx="597" cy="484" r="312" fill="var(--navy)"/>
    <circle cx="181" cy="417" r="202" fill="var(--navy)"/>
    <circle cx="597" cy="484" r="290" fill="url(#poolPhoto)" stroke="var(--white)" stroke-width="2" role="img" aria-label="Photo: technician cleaning a clear turquoise in-ground pool with a lawn and trees behind"/>
    <circle cx="181" cy="417" r="180" fill="url(#spaPhoto)" stroke="var(--white)" stroke-width="2" role="img" aria-label="Photo: hot tub set in a landscaped stone garden beside a timber house"/>

    <!-- bottom bands -->
    <path d="M0 1185 Q180 1150 330 1168 Q470 1190 535 1362 L0 1362 Z" fill="var(--navy)"/>
    <path d="M420 1210 Q600 1150 858 1195 L858 1362 L540 1362 Q500 1270 420 1210 Z" fill="var(--rim)"/>
    <path d="M430 1218 Q610 1160 858 1204 L858 1362 L545 1362 Q505 1275 430 1218 Z" fill="url(#orangeFill)"/>
    <path d="M55 1362 L55 1130 Q60 1085 130 1085 Q200 1088 205 1140 L235 1362 Z" fill="url(#portraitPhoto)" role="img" aria-label="Portrait photo of the pool service owner"/>
  </svg>

  <div class="brand">
    <span class="brand-dot"></span>
    <span class="brand-name">TIDEWELL<br>POOL SERVICE</span>
  </div>

  <h1 class="headline">
    <span class="headline-top">Dive into professional</span>
    <span class="headline-main">Pool service &amp; repair</span>
  </h1>

  <section class="benefits">
    <h2>The benefits to choosing<br>Tidewell Pool Service</h2>
    <ul>
      <li>We have staff on Island a minimum of 3 days a week (April Thru Oct) with an on island shop and vehicle.</li>
      <li>Emergencies situations are quickly handled and difficult issues that are bound to arise, dealt with ease.</li>
      <li>We have great relationships with pool builders that have built on island for needed assistance on larger projects.</li>
    </ul>
  </section>

  <section class="services">
    <h3>Our services</h3>
    <ul>
      <li><svg width="20" height="20" viewBox="0 0 20 20"><circle cx="10" cy="10" r="8.5" fill="none" stroke="var(--orange)" stroke-width="1.6"/><path d="M5.5 10 L9 13.5 L17 4" fill="none" stroke="var(--orange)" stroke-width="2" stroke-linecap="round"/></svg>Pool opening and closing</li>
      <li><svg width="20" height="20" viewBox="0 0 20 20"><circle cx="10" cy="10" r="8.5" fill="none" stroke="var(--orange)" stroke-width="1.6"/><path d="M5.5 10 L9 13.5 L17 4" fill="none" stroke="var(--orange)" stroke-width="2" stroke-linecap="round"/></svg>Renovation</li>
      <li><svg width="20" height="20" viewBox="0 0 20 20"><circle cx="10" cy="10" r="8.5" fill="none" stroke="var(--orange)" stroke-width="1.6"/><path d="M5.5 10 L9 13.5 L17 4" fill="none" stroke="var(--orange)" stroke-width="2" stroke-linecap="round"/></svg>Weekly pool service</li>
      <li><svg width="20" height="20" viewBox="0 0 20 20"><circle cx="10" cy="10" r="8.5" fill="none" stroke="var(--orange)" stroke-width="1.6"/><path d="M5.5 10 L9 13.5 L17 4" fill="none" stroke="var(--orange)" stroke-width="2" stroke-linecap="round"/></svg>Electronic leak detection</li>
      <li><svg width="20" height="20" viewBox="0 0 20 20"><circle cx="10" cy="10" r="8.5" fill="none" stroke="var(--orange)" stroke-width="1.6"/><path d="M5.5 10 L9 13.5 L17 4" fill="none" stroke="var(--orange)" stroke-width="2" stroke-linecap="round"/></svg>Equipment repair and upgrades</li>
    </ul>
  </section>

  <div class="contact">
    Specializing in<br>High-end gunite pools<br>401-555-0187<br><span class="web">www.tidewellnb.com</span>
  </div>

  <div class="offer">We offer free estimates and<br>a satisfaction guarantee!</div>
  <div class="social"><span></span><span></span></div>
</div>
</body>
</html>
```